A WEBSITE FOR A JEWELLERY RETAIL STORE WITH A SHOPPING CART, AND ABILITY TO ORDER ONLINE.

I require a website with a shopping cart.

We sell MAINLY diamond jewellery (such as rings etc). I need it to be simple to change prices with only a few buttons, as the price fluctuates due to the US Dollar.

We are a diamond wholesaler, selling directly to the public, so we guarantee the lowest prices in Australia.

There is also a link to current inventory that will need to be uploaded to the site.

This could be an ongoing job, where you will be paid weekly to maintain and update the website if you wish.

Target Market(s)

People getting engaged, and wanting to buy a diamond ring.

Number of Pages Required

5+ page

Colors

Designer to choose colors to be used in the design.

Requirements
Must have
• elegant.
• modern.
• professional.
• SHOPPING CART.
• ABILITY TO SEARCH FOR LOOSE DIAMONDS (LINK THAT NEEDS TO BE EMBEDDED WILL BE SENT WHICH SHOWS CURRENT STOCK).
• ENGAGEMENT RINGS
• WEDDING RINGS
• DIAMOND EARRINGS
• DIAMOND PENDANTS
• LOOSE DIAMONDS.
• SALE ITEMS.
• OTHER JEWELLERY.
• EDUCATION
• WISH LIST
• CART.
Nice to have
• a good place to look for inspiration on pages is https://www.velmarigems.example.
• YOU MAY VISIT OUR FRIENDWALL PAGE AT.
• HTTP://WWW.SOCIALPAGE.EXAMPLE/QUINTORAJEWELLERS
Should not have
• We don't want it too busy.

```html
<!DOCTYPE html>
<html lang="en">
<head>
<meta charset="utf-8">
<title>Quintora Jewellers – Engagement Rings</title>
<link href="https://fonts.googleapis.com/css2?family=Oranienbaum&family=Raleway:wght@300;400&display=swap" rel="stylesheet">
<style>
:root{
  --ink:#1a1a1a;
  --paper:#ffffff;
  --panel:#d9d9d9;
  --search:#d4d4d4;
  --black:#000000;
  --red:#ec1c24;
  --footer:#050505;
}
*{box-sizing:border-box;margin:0;padding:0}
html,body{width:960px;height:1200px;overflow:hidden;background:var(--paper)}
body{position:relative;font-family:"Oranienbaum",serif;color:var(--ink)}
.abs{position:absolute}
.brand{left:114px;top:11px;font-size:13px;letter-spacing:-.2px;white-space:nowrap}
.main-nav{left:246px;top:25px;display:flex;gap:17px;font-size:8.2px;letter-spacing:-.2px;white-space:nowrap}
.cart{left:853px;top:10px}
.cart-badge{left:872px;top:8px;width:9px;height:9px;border-radius:50%;background:var(--red);color:#fff;font:6px/9px "Raleway",sans-serif;text-align:center}
.account{left:900px;top:10px}
.search{left:258px;top:73px;width:420px;height:28px;background:var(--search);color:#fff;font:300 19px/28px "Raleway",sans-serif;padding-left:24px}
.search-btn{left:678px;top:73px;width:83px;height:28px;background:var(--black);display:flex;align-items:center;justify-content:center}
.filter{left:30px;width:162px;background:var(--panel)}
.filter h2{font-weight:400;font-size:20px;text-decoration:underline;text-align:center;padding-top:3px;line-height:22px}
.filter .sub{font-size:12px;padding-left:48px;margin-top:1px}
.filter ul{list-style:none;padding-left:19px}
.filter li{display:flex;align-items:center;height:24px;font-size:11.5px}
.filter.price li{font:300 11px "Raleway",sans-serif;letter-spacing:-.3px}
.box{width:10px;height:10px;background:#fff;margin-right:19px;position:relative;flex:none}
.box svg{position:absolute;left:-1px;top:-3px}
.product{width:190px;text-align:center}
.product .photo{margin:0 auto;height:154px}
.product h3{font-weight:400;font-size:19px;margin-top:18px;line-height:22px;letter-spacing:-.3px}
.product .cost{font-size:19px;margin-top:7px;line-height:22px}
.buy{display:block;width:96px;height:38px;margin:9px auto 0;background:var(--red);color:#fff;font-size:19px;line-height:38px;text-decoration:none}
.gem-square{width:154px;background:linear-gradient(135deg,#eaf3f7,#9fb6c2 40%,#f4f8fa 60%,#6f8893)}
.gem-round{width:146px;border-radius:50%;background:radial-gradient(circle,#f3f4f7,#c4c7d0 55%,#8e93a0)}
.ring-white{width:140px;background:radial-gradient(ellipse at 50% 40%,#dcdcdc,#f4f4f4 60%,#fff)}
.ring-gold{width:140px;background:radial-gradient(ellipse at 50% 40%,#d9c98a,#ededed 55%,#fff)}
.footer{left:0;top:1030px;width:960px;height:170px;background:linear-gradient(180deg,var(--footer) 0%,#1c1c1c 45%,#8a8a8a 60%,#2a2a2a 72%,var(--footer) 100%)}
.foot-brand{left:120px;top:1045px;display:flex;align-items:center;gap:4px;color:#fff}
.foot-brand i{width:9px;height:9px;background:#fff;display:block;flex:none}
.foot-brand .name{display:flex;flex-direction:column;line-height:1}
.foot-brand .name b{font-weight:400;font-size:12px}
.foot-brand .name small{font-size:5.5px;letter-spacing:2.6px;margin-top:2px}
.foot-nav{left:198px;top:1048px;display:flex;gap:17px;color:#fff;font-size:8.2px;letter-spacing:-.2px;white-space:nowrap}
.social{left:742px;top:1070px;display:flex;gap:10px;color:#fff;font:400 9px "Raleway",sans-serif}
.email{left:327px;top:1158px;width:262px;height:32px;background:#fff;font:400 11px/32px "Raleway",sans-serif;padding-left:27px}
.subscribe{left:589px;top:1158px;width:57px;height:32px;background:var(--red);color:#fff;font:400 11px/32px "Raleway",sans-serif;text-align:center}
</style>
</head>
<body>
<header>
  <div class="abs brand">QUINTORA JEWELLERS</div>
  <nav class="abs main-nav">
    <span>ENGAGEMENT RINGS</span><span>WEDDING RINGS</span><span>DIAMOND EARRINGS</span><span>DIAMOND PENDANTS</span><span>LOOSE DIAMONDS</span><span>SALE ITEMS</span><span>OTHER JEWELLERY</span><span>EDUCATION</span><span>WISH LIST</span>
  </nav>
  <svg class="abs cart" width="22" height="26" viewBox="0 0 22 26"><path d="M2 8h18v16H2z" fill="none" stroke="#555" stroke-width="1"/><path d="M7 8V5a4 4 0 0 1 8 0v3" fill="none" stroke="#555" stroke-width="1"/></svg>
  <div class="abs cart-badge">2</div>
  <svg class="abs account" width="26" height="26" viewBox="0 0 26 26"><circle cx="13" cy="13" r="13" fill="#bbb"/><circle cx="13" cy="10" r="4.5" fill="#fff"/><path d="M5 21a8 6 0 0 1 16 0z" fill="#fff"/></svg>
</header>

<div class="abs search">Search For Products</div>
<div class="abs search-btn"><svg width="22" height="22" viewBox="0 0 22 22"><circle cx="10" cy="9" r="7" fill="none" stroke="#fff" stroke-width="1.3"/><path d="M15 14l5 5" stroke="#fff" stroke-width="1.3"/></svg></div>

<aside class="abs filter" style="top:135px;height:190px">
  <h2>Categories</h2>
  <div class="sub">View all products</div>
  <ul style="margin-top:6px">
    <li><span class="box"><svg width="12" height="12" viewBox="0 0 12 12"><path d="M2 6l3 3 6-8" fill="none" stroke="#000" stroke-width="1.6"/></svg></span>ENGAGEMENT RINGS</li>
    <li><span class="box"></span>LOOSE DIAMONDS</li>
    <li><span class="box"></span>EARRINGS</li>
    <li><span class="box"></span>BRACELETS</li>
    <li><span class="box"></span>NECKLACES</li>
    <li><span class="box"></span>SILVER JEWELLERY</li>
  </ul>
</aside>

<aside class="abs filter price" style="top:346px;height:170px">
  <h2>Price</h2>
  <ul style="margin-top:4px">
    <li><span class="box"><svg width="12" height="12" viewBox="0 0 12 12"><path d="M2 6l3 3 6-8" fill="none" stroke="#000" stroke-width="1.6"/></svg></span>$1,000-$3,000</li>
    <li><span class="box"></span>$4,000-$5,000</li>
    <li><span class="box"></span>$6,000-$9,000</li>
    <li><span class="box"></span>$10,000-$18,000</li>
    <li><span class="box"></span>$19,000-$30,000</li>
    <li><span class="box"></span>$40,000&amp; Up</li>
  </ul>
</aside>

<main>
  <article class="abs product" style="left:199px;top:130px"><div class="photo gem-square" role="img" aria-label="Princess cut diamond photo"></div><h3>Carat Marquise Diamond</h3><p class="cost">$ 1,900</p><a class="buy" href="#">Buy Now</a></article>
  <article class="abs product" style="left:439px;top:130px"><div class="photo gem-round" role="img" aria-label="Round brilliant diamond photo"></div><h3>1CT QGL ROUND D SI2</h3><p class="cost">$4,900</p><a class="buy" href="#">Buy Now</a></article>
  <article class="abs product" style="left:661px;top:130px"><div class="photo ring-white" role="img" aria-label="White gold diamond engagement ring photo"></div><h3>1CT QGL ROUND D SI2</h3><p class="cost">$4,900</p><a class="buy" href="#">Buy Now</a></article>

  <article class="abs product" style="left:199px;top:443px"><div class="photo ring-gold" role="img" aria-label="Yellow gold diamond engagement ring photo"></div><h3>Carat Marquise Diamond</h3><p class="cost">$ 1,900</p><a class="buy" href="#">Buy Now</a></article>
  <article class="abs product" style="left:439px;top:443px"><div class="photo gem-round" role="img" aria-label="Round brilliant diamond photo"></div><h3>1CT QGL ROUND D SI2</h3><p class="cost">$4,900</p><a class="buy" href="#">Buy Now</a></article>
  <article class="abs product" style="left:661px;top:443px"><div class="photo ring-white" role="img" aria-label="White gold diamond engagement ring photo"></div><h3>1CT QGL ROUND D SI2</h3><p class="cost">$4,900</p><a class="buy" href="#">Buy Now</a></article>

  <article class="abs product" style="left:199px;top:740px"><div class="photo gem-square" role="img" aria-label="Princess cut diamond photo"></div><h3>Carat Marquise Diamond</h3><p class="cost">$ 1,900</p><a class="buy" href="#">Buy Now</a></article>
  <article class="abs product" style="left:439px;top:740px"><div class="photo gem-round" role="img" aria-label="Round brilliant diamond photo"></div><h3>1CT QGL ROUND D SI2</h3><p class="cost">$4,900</p><a class="buy" href="#">Buy Now</a></article>
  <article class="abs product" style="left:661px;top:740px"><div class="photo ring-white" role="img" aria-label="White gold diamond engagement ring photo"></div><h3>1CT QGL ROUND D SI2</h3><p class="cost">$4,900</p><a class="buy" href="#">Buy Now</a></article>
</main>

<footer>
  <div class="abs footer" role="img" aria-label="Scattered diamonds on a dark reflective surface"></div>
  <div class="abs foot-brand"><i></i><span class="name"><b>QUINTORA</b><small>JEWELLERS</small></span></div>
  <nav class="abs foot-nav">
    <span>ENGAGEMENT RINGS</span><span>WEDDING RINGS</span><span>DIAMOND EARRINGS</span><span>DIAMOND PENDANTS</span><span>LOOSE DIAMONDS</span><span>SALE ITEMS</span><span>OTHER JEWELLERY</span><span>EDUCATION</span><span>WISH LIST</span>
  </nav>
  <div class="abs social"><span>Friendwall</span><span>Chirper</span><span>Pictura</span></div>
  <div class="abs email">Type Email</div>
  <div class="abs subscribe">Subscribe</div>
</footer>
</body>
</html>
```